12 Meter Banner-Design Lagerhalle
Zielgruppe
Wir errichten neue Elektroanlagen für Einfamilenhäuser und Wohnungen.
Hallo,
wir möchten auf 12 Meter drei Banner spannen um die unschönen Rohre und Kabel zu verdecken. Jeder der drei Banner soll 400cm breit und 160cm hoch werden.
-Banner 1 links: Motivationsspruch groß, mittig - : Wer immer tut, was er schon kann, bleibt immer das, was er schon ist.
- Banner 2 mitte : Komfortzone ( Grafiken habe ich im Anhang von dem Aufbau der Komfortzone ) Toll wäre ein selbst erstelltes Design passend zum Unternehmen / Farben Schriftart etc.
-Banner 3 rechts: Motivationsspruch : Zusammenkommen ist ein Beginn, zusammenbleiben ist ein Fortschritt, zusammenarbeiten ist ein Erfolg.
- Design nach Vorgabe Druckpilot ( Datasheet) erstellen
Gundsätzlich wäre super, wenn alle 3 Designs/ Banner miteinander harmonieren. Alles andere ist der Kreativität überlassen.
Schriftart: Fira Sans / Montserrat
Wir würden uns über eine Zusammenarbeit freuen.
Beste Grüße

```html
<!DOCTYPE html>
<html lang="de">
<head>
<meta charset="utf-8">
<title>Banner-Serie Lagerhalle</title>
<link rel="stylesheet" href="https://fonts.googleapis.com/css2?family=Montserrat:ital,wght@0,300;0,400;0,600;0,700;0,800;1,400&display=swap">
<style>
  :root {
    --brand-blue: #0087c9;
    --zone-mid: #1f9edd;
    --zone-light: #4ebef3;
    --comfort-white: #f7f7f7;
    --panel-grey: #f3f3f3;
    --accent-cyan: #9fe1fb;
    --white: #ffffff;
    --page: #ffffff;
  }
  html, body {
    margin: 0;
    padding: 0;
    width: 702px;
    height: 1200px;
    overflow: hidden;
    background: var(--page);
    font-family: "Montserrat", sans-serif;
  }
  .sheet { position: relative; width: 702px; height: 1200px; }
  .banner {
    position: absolute;
    box-shadow: 0 3px 10px rgba(0, 60, 110, 0.18);
    line-height: 0;
  }
  .banner svg { width: 100%; height: 100%; display: block; }
  .banner--thumb { top: 46px; width: 217px; height: 87px; }
  .banner--thumb.is-quote-left { left: 18px; }
  .banner--thumb.is-zones { left: 241px; }
  .banner--thumb.is-quote-right { left: 463px; }
  .banner--large { left: 68px; width: 569px; height: 227px; }
  .banner--large.is-quote-left { top: 277px; }
  .banner--large.is-zones { top: 556px; }
  .banner--large.is-quote-right { top: 835px; left: 71px; width: 568px; }

  .bg-blue { fill: var(--brand-blue); }
  .bg-grey { fill: var(--panel-grey); }
  .frame-line { fill: none; stroke: var(--white); stroke-width: 5; }
  .quote-bold { font-family: "Montserrat", sans-serif; font-weight: 700; font-size: 60px; fill: var(--white); }
  .quote-light { font-family: "Montserrat", sans-serif; font-weight: 300; font-size: 60px; fill: var(--accent-cyan); }
  .zone-outer { fill: var(--zone-mid); }
  .zone-fear { fill: var(--zone-light); }
  .zone-comfort { fill: var(--comfort-white); }
  .zone-title { font-family: "Montserrat", sans-serif; font-weight: 700; font-size: 20px; fill: var(--white); }
  .zone-title.is-dark { fill: var(--brand-blue); }
  .zone-item { font-family: "Montserrat", sans-serif; font-style: italic; font-weight: 400; font-size: 16px; fill: var(--white); }
  .zone-item.is-dark { fill: var(--brand-blue); }
  .side-label { font-family: "Montserrat", sans-serif; font-weight: 700; font-size: 25px; letter-spacing: 6px; }
  .side-label.is-blue { fill: var(--brand-blue); }
  .side-label.is-white { fill: var(--white); }
  .chevron { fill: none; stroke: var(--white); stroke-width: 4; stroke-linecap: round; stroke-linejoin: round; }
  .step-lead { font-family: "Montserrat", sans-serif; font-weight: 400; font-size: 28px; fill: var(--white); }
  .step-word { font-family: "Montserrat", sans-serif; font-weight: 800; font-size: 52px; letter-spacing: 9px; fill: var(--accent-cyan); }
</style>
</head>
<body>
<svg width="0" height="0" style="position:absolute" aria-hidden="true">
  <defs>
    <symbol id="quote-left" viewBox="0 0 1203 481">
      <rect class="bg-blue" width="1203" height="481"/>
      <path class="frame-line" d="M734 144 H896 V226"/>
      <path class="frame-line" d="M269 252 V331 H431"/>
      <text class="quote-bold" x="217" y="169">Wer immer tut,</text>
      <text class="quote-bold" x="217" y="227">was er schon kann,</text>
      <text class="quote-light" x="466" y="306">bleibt immer das,</text>
      <text class="quote-light" x="466" y="364">was er schon ist.</text>
    </symbol>
    <symbol id="zones" viewBox="0 0 1203 481">
      <rect class="bg-grey" width="1203" height="481"/>
      <path class="bg-blue" d="M326 0 H1203 V481 H324 Q153 240 326 0 Z"/>
      <ellipse class="zone-outer" cx="520" cy="241" rx="280" ry="204"/>
      <ellipse class="zone-fear" cx="418" cy="239" rx="178" ry="135"/>
      <circle class="zone-comfort" cx="338" cy="240" r="83"/>
      <text class="side-label is-blue" transform="translate(141 240) rotate(-90)" text-anchor="middle">KOMFORTZONE</text>
      <text class="side-label is-white" transform="translate(1169 240) rotate(-90)" text-anchor="middle">UNTERNEHMENSVISION</text>
      <text class="zone-title is-dark" x="287" y="220">KOMFORT</text>
      <text class="zone-item is-dark" x="287" y="240">Kontrolle</text>
      <text class="zone-item is-dark" x="287" y="259">Gewohnheit</text>
      <text class="zone-item is-dark" x="287" y="276">Routine</text>
      <text class="zone-title" x="434" y="220">ANGSTZONE</text>
      <text class="zone-item" x="434" y="240">Unsicherheit</text>
      <text class="zone-item" x="434" y="259">Ablehnung</text>
      <text class="zone-item" x="434" y="276">Ausreden</text>
      <text class="zone-title" x="616" y="220">LERNZONE</text>
      <text class="zone-item" x="616" y="240">Neue Skills</text>
      <text class="zone-item" x="616" y="259">Erfahrung</text>
      <text class="zone-item" x="616" y="276">Selbstvertrauen</text>
      <text class="zone-title" x="828" y="220">WACHSTUMSZONE</text>
      <text class="zone-item" x="828" y="240">Zielerreichung</text>
      <text class="zone-item" x="828" y="259">Selbstsicherheit</text>
      <text class="zone-item" x="828" y="276">Zufriedenheit</text>
      <path class="chevron" d="M1088 224 L1104 241 L1088 258"/>
    </symbol>
    <symbol id="quote-right" viewBox="0 0 1203 481">
      <rect class="bg-blue" width="1203" height="481"/>
      <path class="frame-line" d="M320 113 H270 V372 H320"/>
      <path class="frame-line" d="M731 113 H925 V372 H755"/>
      <text class="step-lead" x="360" y="108">Zusammenkommen</text>
      <text class="step-lead" x="360" y="136">ist ein</text>
      <text class="step-word" x="452" y="160">BEGINN</text>
      <text class="step-lead" x="360" y="228">Zusammenbleiben</text>
      <text class="step-lead" x="360" y="256">ist ein</text>
      <text class="step-word" x="452" y="281">FORTSCHRITT</text>
      <text class="step-lead" x="360" y="349">Zusammenarbeiten</text>
      <text class="step-lead" x="360" y="377">ist ein</text>
      <text class="step-word" x="452" y="398">ERFOLG.</text>
    </symbol>
  </defs>
</svg>

<main class="sheet">
  <section class="banner banner--thumb is-quote-left"><svg viewBox="0 0 1203 481" preserveAspectRatio="none"><use href="#quote-left"/></svg></section>
  <section class="banner banner--thumb is-zones"><svg viewBox="0 0 1203 481" preserveAspectRatio="none"><use href="#zones"/></svg></section>
  <section class="banner banner--thumb is-quote-right"><svg viewBox="0 0 1203 481" preserveAspectRatio="none"><use href="#quote-right"/></svg></section>

  <section class="banner banner--large is-quote-left"><svg viewBox="0 0 1203 481" preserveAspectRatio="none"><use href="#quote-left"/></svg></section>
  <section class="banner banner--large is-zones"><svg viewBox="0 0 1203 481" preserveAspectRatio="none"><use href="#zones"/></svg></section>
  <section class="banner banner--large is-quote-right"><svg viewBox="0 0 1203 481" preserveAspectRatio="none"><use href="#quote-right"/></svg></section>
</main>
</body>
</html>
```